Relaunch of company website (Technical company)

Hi all,

we need a website based on Wordpress who makes the customer curious and excited of all the possibilities we can offer.
Customers are B2B. The layout should be based on the screenshots I added, but refreshed and modernized with some nice gadgets.
All needs to be responsive for the different devices.
We are a technical company. We provide a full range of service from 3D scan, Manufacturing, Prototyping, Bulk production and CAD service.

Later the website needs to have a multi language option.

Home:

1. Logo top left (attached)
2. Menu bar top right
3. Header picture like in the screenshot
4. Than the three small blue pics (CAD - Fertigung - Manufaktur) we want a
hoover-small zoom effect as soon as the mouse hits them.
5. Introduction text of our company
6. Contact Information (Design sample see attachment)
7. At the end "Impressum - Datenschutzerklärung - Haftungsausschluss. Those need to be linked to extra pages where we can add mandatory text (Legal notice, Privacy, Disclaimer)

Leistungen - Our service:

1. See the attachment named our service.
2. First on page a gallery where we can add pictures. If moving the mouse over the picture we want a one line explanation e.g. 3D Scan, Production, Die cast...
no click option at the pictures, just to see.
3. Below that, a side menu (we need to add or remove items by our self if necessary) on the left where we can add our service.
4. If the customer is clicking a service, it needs to be highlighted
5. After clicking a service we want our text to that service appear right of the menu (see attachment sample) and 2 big pictures on top of the menu and text field.

Gallery:

1. Headline pictures for each gallery Category (6-8 at the moment)
2. Mouse over the picture zooms it a little in and adds a text what category it is
e.g. Reverse engineering, Prototyping, Laserscan
3. Clicking on the picture opens the detail gallery to that category. There we need
to add pictures specific to that service.
4. If the customer is clicking on a picture from there, all pictures from that
Category will open in a full screen view mode

Blog:

1. A blog to add news (picture and text). Right now we don´t have the time to feed
it, so we want to deactivate it as long as we cant keep it up to date. Later it
should be part of the website.

Unternehmen:

1. Drop down menu: Our Team - History - Unsere Partner - AGB - Impressum

Our Team:
1. Short description of our employees including picture (see attachment)
2. Contact Information (Design sample see attachment)
3. At the end "Impressum - Datenschutzerklärung - Haftungsausschluss. Those need to be linked to extra pages where we can add mandatory text (Legal notice, Privacy, Disclaimer)

History:
1. Timeline where we can add milestones including date, and pictures of the company (see screenshot)

Unsere Partner:
1. Text field where we can introduce our partners including pictures if necessary.

A blog would be a nice option, social media shortcuts to Instagram-FB but no preview of FB Timeline within the website.

We do have professional text already, that will be added by us. We expect you to use any sample text and pictures for the draft, beside what we supply already.

If you see the need of buying pictures from Quorvane or any other picture company that is OK for us.

What we expect:

A modern, fresh website based on our existing design, changes are fine as long as the whole website design does not change completely to an unicorn thing in pink. Feel free to be creative. New ideas will be discussed, we are open to good ideas. We don´t stick fix to our idea, but we want our customers can see that its still the same company.
Scrolling effects would be a nice gadget if possible.

We have a bad page already...don´t want a second bad one :-)

Our company blue is RBG 106, 206, 224

Greets to all, looking for professional results.

Target Market(s)

B2B, Engineering companys,

Industry/Entity Type

Technical Service

Number of Pages Required

5+ page

Font styles to use
Sans Serif
Other font styles liked:
• verdana

Colors
0455a3
000000
ffffff

Requirements
Must have
• Responsive design, We want to be able to add posts to the Blog, pictures to the categories, and categories by ourself if necessary. (Wordpress)
• Lets say we want to add one more category at „Leistungen-Our Service“ that should be possible for us in the wordpress background.
Nice to have
• Dynamic elements to make the website more alive.
Should not have
• Sliders, Contact form

```html
<!DOCTYPE html>
<html lang="en">
<head>
<meta charset="utf-8">
<title>Vantor Precision – Home</title>
<link href="https://fonts.googleapis.com/css2?family=Montserrat:wght@300;400;500;600;700&display=swap" rel="stylesheet">
<style>
:root{
  --brand:#6acee0;
  --brand-dark:#3fb4cb;
  --ink:#1d2126;
  --text:#5d636b;
  --muted:#9aa0a8;
  --pale:#f3f5f8;
  --band:#4b525d;
  --backdrop:#dcdcde;
  --white:#ffffff;
  --line:#e3e6ea;
}
*{box-sizing:border-box;margin:0;padding:0}
html,body{width:1200px;height:2970px;overflow:hidden}
body{background:var(--backdrop);font-family:"Montserrat",Verdana,sans-serif;color:var(--text)}
.page{position:absolute;left:105px;top:0;width:990px;height:2970px;background:var(--white);overflow:hidden}
.abs{position:absolute}
.pill{position:absolute;height:22px;border:1px solid var(--line);border-radius:11px;font-size:8px;letter-spacing:1.5px;line-height:20px;text-align:center;color:var(--muted);background:var(--white)}
.link{font-size:8px;letter-spacing:1.5px;color:var(--brand);font-weight:500;display:flex;align-items:center;gap:6px}
.link .dot{width:11px;height:11px;border:1px solid var(--brand);border-radius:50%;display:inline-block}
.para{font-size:10px;line-height:1.55;color:var(--muted)}

/* header */
.logo{left:28px;top:22px;display:flex;align-items:center;gap:8px;font-size:15px;font-weight:500;color:var(--ink);letter-spacing:1px}
.logo .mark{width:22px;height:22px;border:1.5px solid var(--brand);border-radius:50%}

/* hero */
.hero-left{left:0;top:0;width:650px;height:430px;background:var(--pale)}
.hero-right{left:650px;top:0;width:340px;height:430px;background:var(--brand)}
.hero-rule{left:48px;top:145px;width:1px;height:190px;background:var(--line)}
.hero-title{left:64px;top:150px;width:230px;font-size:16px;font-weight:700;color:var(--ink);line-height:1.3}
.hero-text{left:64px;top:200px;width:210px}
.hero-link{left:64px;top:290px}
.hero-art{left:300px;top:80px;width:320px;height:290px;border-radius:4px;background:linear-gradient(160deg,#e4e6e9 0%,#a3a8af 38%,#5c6169 55%,#b9bdc3 75%,#dfe2e6 100%)}
.hero-part{left:690px;top:95px;width:270px;height:270px;border-radius:4px;background:linear-gradient(150deg,#cdeff5 0%,#9adde9 40%,#3fb0c6 62%,#8fd6e4 100%)}
.slide-nav{left:637px;top:206px;width:26px;height:26px;border-radius:50%;background:var(--white);display:flex;align-items:center;justify-content:center;box-shadow:0 2px 6px rgba(0,0,0,.1)}
.slide-count{left:672px;top:213px;font-size:9px;color:var(--white);letter-spacing:1px}
.legend{left:585px;top:350px;font-size:6px;color:var(--muted);line-height:1.6}
.legend span{display:inline-block;width:5px;height:5px;margin-right:4px}
.scroll-down{left:30px;top:400px;width:30px;height:30px;border-radius:50%;background:#7d838c;display:flex;align-items:center;justify-content:center}

/* intro */
.intro-bg{left:0;top:430px;width:725px;height:345px;background:var(--pale)}
.intro-title{left:64px;top:518px;width:420px;font-size:15px;font-weight:700;color:var(--ink);line-height:1.35}
.intro-sub{left:64px;top:592px;font-size:11px;color:var(--text)}
.intro-btn{left:64px;top:626px;width:112px}
.intro-photo{left:527px;top:605px;width:400px;height:280px;background:linear-gradient(150deg,#1f2124 0%,#55595e 30%,#c9cccf 50%,#7d8186 65%,#2c2e31 100%);box-shadow:0 10px 30px rgba(0,0,0,.15)}

/* services */
.service{position:absolute;top:960px;width:280px}
.service .rule{position:absolute;left:0;top:65px;width:1px;height:120px;background:var(--line)}
.service h3{margin-top:50px;font-size:13px;font-weight:700;color:var(--ink)}
.service .para{margin-top:6px;width:250px}
.service .link{margin-top:12px}

/* company band */
.band{left:0;top:1272px;width:990px;height:335px;background:var(--band)}
.band-card{left:0;top:1330px;width:466px;height:340px;background:var(--white);box-shadow:0 10px 30px rgba(0,0,0,.15)}
.band-art{left:30px;top:1350px;width:406px;height:300px;background:linear-gradient(155deg,#f1f2f4 0%,#b7bbc1 30%,#5f646c 50%,#c8cbd0 68%,#eef0f2 100%)}
.band-title{left:527px;top:1390px;width:420px;font-size:14px;font-weight:600;color:var(--white);line-height:1.35}
.band-text{left:527px;top:1460px;width:400px;color:#c3c7cd}
.band-btn{left:527px;top:1553px;width:112px;height:22px;border-radius:11px;background:var(--brand);color:var(--white);font-size:8px;letter-spacing:1.5px;line-height:22px;text-align:center}

/* blog */
.blog-bg{left:0;top:1670px;width:990px;height:534px;background:var(--pale)}
.blog-heading{left:0;top:1760px;width:990px;text-align:center;font-size:13px;font-weight:600;color:var(--ink)}
.post{position:absolute;top:1803px;width:248px}
.post .thumb{width:248px;height:157px}
.post .date{margin-top:16px;font-size:7px;letter-spacing:1px;color:var(--muted)}
.post h4{margin-top:6px;font-size:11px;font-weight:700;color:var(--ink);line-height:1.35}
.post .para{margin-top:8px}
.post .link{margin-top:20px}

/* finder */
.finder-title{left:64px;top:2330px;font-size:31px;font-weight:300;color:var(--ink)}
.finder-sub{left:64px;top:2376px;font-size:11px;color:var(--text)}
.finder-rule{left:520px;top:2330px;width:1px;height:190px;background:var(--line)}
.finder-list{left:527px;top:2338px;list-style:none}
.finder-list li{font-size:13px;font-weight:600;letter-spacing:1px;color:var(--brand);display:flex;align-items:center;gap:8px;height:29px}
.finder-list li.muted{color:var(--muted)}
.finder-list li.gap{margin-top:29px}
.finder-list .dot{width:14px;height:14px;border:1.5px solid currentColor;border-radius:50%}

/* footer */
.footer{left:0;top:2568px;width:990px;height:402px;background:var(--pale);text-align:center}
.footer h5{margin-top:100px;font-size:12px;font-weight:700;color:var(--ink)}
.footer .phone{margin-top:22px;font-size:13px;color:var(--muted)}
.footer .mail{margin-top:4px;font-size:11px;color:var(--brand)}
.footer .name{margin-top:22px;font-size:10px;color:var(--ink)}
.footer .addr{margin-top:4px;font-size:9px;color:var(--muted)}
.socials{margin:22px auto 0;display:flex;justify-content:center;gap:10px}
.socials span{width:18px;height:18px;border:1px solid #c9cdd3;border-radius:50%;display:block}
.footer .rule{margin:26px 30px 0;height:1px;background:var(--line)}
.legal{margin-top:28px;font-size:7px;letter-spacing:1.5px;color:var(--brand);display:flex;justify-content:center;gap:40px}
.legal i{font-style:normal;color:var(--muted)}
</style>
</head>
<body>
<div class="page">

  <!-- hero -->
  <div class="abs hero-left"></div>
  <div class="abs hero-right"></div>

  <header>
    <div class="abs logo"><span class="mark"></span>Vantor Precision</div>
    <div class="pill" style="left:608px;top:21px;width:92px">CONTACT</div>
    <div class="pill" style="left:796px;top:21px;width:62px">ENG ⌄</div>
    <div class="pill" style="left:868px;top:21px;width:94px;text-align:left;padding-left:18px">MENU</div>
    <div class="abs" style="left:940px;top:21px;width:22px;height:22px;border-radius:50%;background:#6f757e"></div>
  </header>

  <div class="abs hero-art" role="img" aria-label="Exploded technical illustration of a motor assembly"></div>
  <div class="abs hero-part" role="img" aria-label="Machined gear part on a blue drawing background"></div>
  <div class="abs hero-rule"></div>
  <h1 class="abs hero-title">Lorem Ipsum is simply dummy text</h1>
  <p class="abs hero-text para">Sed ut perspiciatis unde omnis iste natus error sit voluptatem accusantium doloremque laudantium, totam rem aperiam, eaque ipsa quae ab illo inventore veritatis.</p>
  <a class="abs hero-link link">DISCOVER MORE <span class="dot"></span></a>
  <div class="abs slide-nav"><svg width="10" height="10" viewBox="0 0 10 10"><path d="M3 1l4 4-4 4" fill="none" stroke="#6acee0" stroke-width="1.4"/></svg></div>
  <div class="abs slide-count">01 / 06</div>
  <div class="abs legend"><div><span style="background:#4b525d"></span>Metal</div><div><span style="background:#9aa0a8"></span>Part</div><div><span style="background:#e0484d"></span>Core</div></div>
  <div class="abs scroll-down"><svg width="10" height="10" viewBox="0 0 10 10"><path d="M1 3l4 4 4-4" fill="none" stroke="#fff" stroke-width="1.4"/></svg></div>

  <!-- intro -->
  <div class="abs intro-bg"></div>
  <h2 class="abs intro-title">We provide a full range of service from 3D scan, Manufacturing, Prototyping, Bulk production and CAD service</h2>
  <p class="abs intro-sub">Website have a multi language option</p>
  <div class="pill intro-btn" style="color:var(--brand)">EXPLORE MORE</div>
  <div class="abs intro-photo" role="img" aria-label="Milling machine cutting a metal workpiece"></div>

  <!-- services -->
  <div class="service" style="left:64px">
    <svg class="abs" style="top:0" width="34" height="30" viewBox="0 0 34 30"><path d="M2 28L9 4l7 24M18 28l7-24 7 24M2 4h30" fill="none" stroke="#6acee0" stroke-width="2"/></svg>
    <div class="rule"></div>
    <h3>CAD service</h3>
    <p class="para">Quis nostrud exercitation ullamco laboris nisi ut aliquip ex ea commodo consequat. Duis aute irure dolor in reprehenderit in voluptate velit esse cillum dolore eu fugiat.</p>
    <a class="link">LEARN MORE <span class="dot"></span></a>
  </div>
  <div class="service" style="left:372px">
    <svg class="abs" style="top:0" width="36" height="30" viewBox="0 0 36 30"><circle cx="12" cy="18" r="7" fill="none" stroke="#6acee0" stroke-width="4" stroke-dasharray="3 2.5"/><circle cx="12" cy="18" r="3" fill="#6acee0"/><circle cx="27" cy="8" r="5" fill="none" stroke="#6acee0" stroke-width="3" stroke-dasharray="2.5 2"/></svg>
    <div class="rule"></div>
    <h3>Production</h3>
    <p class="para">Quis nostrud exercitation ullamco laboris nisi ut aliquip ex ea commodo consequat. Duis aute irure dolor in reprehenderit in voluptate velit esse cillum dolore eu fugiat.</p>
    <a class="link">LEARN MORE <span class="dot"></span></a>
  </div>
  <div class="service" style="left:680px">
    <svg class="abs" style="top:0" width="30" height="30" viewBox="0 0 30 30"><path d="M3 9l10-6h14v18l-10 6H3z M3 9h14v18 M17 9l10-6" fill="none" stroke="#6acee0" stroke-width="2"/></svg>
    <div class="rule"></div>
    <h3>Manufacture</h3>
    <p class="para">Quis nostrud exercitation ullamco laboris nisi ut aliquip ex ea commodo consequat. Duis aute irure dolor in reprehenderit in voluptate velit esse cillum dolore eu fugiat.</p>
    <a class="link">LEARN MORE <span class="dot"></span></a>
  </div>

  <!-- company introduction -->
  <div class="abs band"></div>
  <div class="abs band-card"></div>
  <div class="abs band-art" role="img" aria-label="Rendered steel gear coupling over a technical drawing"></div>
  <h2 class="abs band-title">Company introduction lorem ipsum dolor sit amet, sed do eiusmod tempor incididunt ut labore et dolore magna aliqua.</h2>
  <p class="abs band-text para">Lorem ipsum dolor sit amet, consectetur adipisicing elit, sed do eiusmod tempor incididunt ut labore et dolore magna aliqua. Ut enim ad minim veniam, quis nostrud exercitation ullamco laboris nisi ut aliquip ex ea commodo consequat. Duis aute irure dolor in reprehenderit in voluptate velit esse. Excepteur sint occaecat cupidatat non proident.</p>
  <div class="abs band-btn">ABOUT US</div>

  <!-- blog -->
  <div class="abs blog-bg"></div>
  <h2 class="abs blog-heading">Blog / News Atricals</h2>
  <article class="post" style="left:64px">
    <div class="thumb" role="img" aria-label="Close-up of a metal turbine part" style="background:linear-gradient(135deg,#2f3134 0%,#8f9398 45%,#d0d2d5 55%,#45484d 100%)"></div>
    <p class="date">JUN 21, 2018</p>
    <h4>Lorem Ipsum has been the industry's standard dummy text ever</h4>
    <p class="para">Ut enim ad minim veniam, quis nostrud exercitation ullamco laboris nisi ut aliquip ex ea commodo consequat duis aute.</p>
    <a class="link">READ MORE <span class="dot"></span></a>
  </article>
  <article class="post" style="left:372px">
    <div class="thumb" role="img" aria-label="Sand cast metal parts in warm light" style="background:linear-gradient(135deg,#4a3c28 0%,#b99d75 45%,#dcc7a4 55%,#5d4d36 100%)"></div>
    <p class="date">JUN 21, 2018</p>
    <h4>Lorem Ipsum has been the industry's standard dummy text ever</h4>
    <p class="para">Ut enim ad minim veniam, quis nostrud exercitation ullamco laboris nisi ut aliquip ex ea commodo consequat duis aute.</p>
    <a class="link">READ MORE <span class="dot"></span></a>
  </article>
  <article class="post" style="left:680px">
    <div class="thumb" role="img" aria-label="Cast propeller blade on a dark background" style="background:linear-gradient(135deg,#262725 0%,#7f7c6b 45%,#b5b29f 55%,#343531 100%)"></div>
    <p class="date">JUN 21, 2018</p>
    <h4>Lorem Ipsum has been the industry's standard dummy text ever</h4>
    <p class="para">Ut enim ad minim veniam, quis nostrud exercitation ullamco laboris nisi ut aliquip ex ea commodo consequat duis aute.</p>
    <a class="link">READ MORE <span class="dot"></span></a>
  </article>

  <!-- finder -->
  <h2 class="abs finder-title">What are you looking for?</h2>
  <p class="abs finder-sub">Explore all Vantor Precision solutions</p>
  <div class="abs finder-rule"></div>
  <ul class="abs finder-list">
    <li>PRODUCT AND SOLUTIONS <span class="dot"></span></li>
    <li class="muted">BECOME A PARTNER <span class="dot"></span></li>
    <li>OUR SERVICE <span class="dot"></span></li>
    <li class="gap">ABOUT COMPANY <span class="dot"></span></li>
    <li>CONTACT <span class="dot"></span></li>
  </ul>

  <!-- footer -->
  <footer class="abs footer">
    <h5>How to Reach Us</h5>
    <p class="phone">Call Us: +00 (0) 1234 / 56789</p>
    <p class="mail">✉ hello@vantor.example</p>
    <p class="name">Vantor Precision</p>
    <p class="addr">12345 Sampletown, Lorem Ipsum, Germany</p>
    <div class="socials"><span></span><span></span><span></span><span></span></div>
    <div class="rule"></div>
    <div class="legal"><span>LEGAL NOTICE</span><i>|</i><span>PRIVACY</span><i>|</i><span>DISCLAIMER</span></div>
  </footer>

</div>
</body>
</html>
```